Business Card Design Project

We need a simple business card design that uses our current logo.
We need to have the current logo put into a high res format.
We need to have 1 card made with contact information.
We will supply the information for the 4 employees.
Industry/Entity Type
Business
Requirements
Must have
- The contact information is as follows:
Mark Dellweather
Producer/CEO
c. 949-555-0147
f. 650-555-0193
markd@lanternbay.example
Al Vostrand, CFO
c. 949-555-0162
f. 650-555-0193
alv@lanternbay.example
Peter Malvane, PR
c. 267-555-0128
f. 650-555-0193
pmalvane@lanternbay.example
Tim Garrowby, Producer
c. 949-555-0184
f. 650-555-0193
timg@lanternbay.example
The address for all cards is:
318 W Calle Norvento #2715, San Clemente, CA 92681

```html
<!DOCTYPE html>
<html lang="en">
<head>
<meta charset="utf-8">
<title>Lantern Bay Media – Business Card</title>
<link rel="stylesheet" href="https://fonts.googleapis.com/css2?family=Oswald:wght@600&family=Archivo+Narrow:wght@700&family=Archivo:wght@800&display=swap">
<style>
  :root {
    --stage: #4a4a4c;
    --card-dark: #1d1d1f;
    --card-mid: #3a3a3c;
    --edge-light: #b9dcf6;
    --edge-deep: #4f97d3;
    --brand-blue: #6cb4ea;
    --name-blue: #4a92d6;
    --ink-white: #ffffff;
    --label: #ffffff;
  }
  * { margin: 0; padding: 0; box-sizing: border-box; }
  html, body { width: 1200px; height: 750px; overflow: hidden; }
  body { background: var(--stage); position: relative; font-family: "Archivo Narrow", Arial, sans-serif; }

  .card {
    position: absolute;
    width: 540px;
    height: 310px;
    overflow: hidden;
    box-shadow: 0 10px 28px rgba(0,0,0,.45);
  }
  .card--front { left: 50px; top: 80px; }
  .card--back  { left: 610px; top: 320px; }

  .card__paper {
    position: absolute; inset: 0;
    background:
      radial-gradient(ellipse at 30% 25%, var(--card-mid), transparent 60%),
      radial-gradient(ellipse at 75% 70%, #323234, transparent 55%),
      var(--card-dark);
  }
  .card__edge {
    position: absolute; top: 0; bottom: 0; width: 12px;
    background: linear-gradient(90deg, var(--edge-deep), var(--edge-light) 45%, var(--edge-deep));
  }
  .card__edge--left { left: 0; }
  .card__edge--right { right: 0; }

  .brand-name {
    position: absolute;
    font-family: "Oswald", "Arial Narrow", sans-serif;
    font-weight: 600;
    color: var(--brand-blue);
    text-transform: uppercase;
    letter-spacing: 1px;
    white-space: nowrap;
  }
  .card--front .brand-name { left: 80px; top: 108px; font-size: 48px; line-height: 1; }
  .address {
    position: absolute; left: 82px; top: 170px;
    color: var(--ink-white); font-size: 12.5px; letter-spacing: .2px;
  }

  .card--back .brand-name { left: 34px; top: 110px; font-size: 30px; line-height: 1; }
  .divider {
    position: absolute; left: 292px; top: 95px; width: 1.5px; height: 180px;
    background: var(--ink-white); opacity: .85;
  }
  .contact { position: absolute; left: 306px; top: 110px; color: var(--ink-white); }
  .contact__name {
    font-family: "Archivo", Arial, sans-serif; font-weight: 800;
    font-size: 22px; color: var(--name-blue); line-height: 1.1; white-space: nowrap;
  }
  .contact__title { font-size: 14px; margin-top: 3px; }
  .contact__lines { list-style: none; margin-top: 16px; font-size: 11.5px; line-height: 1.45; }

  .side-label {
    position: absolute; color: var(--label);
    font-family: "Archivo Narrow", Arial, sans-serif; font-weight: 700; font-size: 24px;
  }
  .side-label--front { left: 195px; top: 420px; }
  .side-label--back  { left: 820px; top: 665px; }
</style>
</head>
<body>
  <section class="card card--front" aria-label="Card front">
    <div class="card__paper" role="img" aria-label="Crumpled black paper texture"></div>
    <div class="card__edge card__edge--left"></div>
    <div class="card__edge card__edge--right"></div>
    <div class="brand-name">Lantern Bay Media</div>
    <p class="address">318 W Calle Norvento #2715, San Clemente, CA 92681</p>
  </section>
  <p class="side-label side-label--front">front</p>

  <section class="card card--back" aria-label="Card back">
    <div class="card__paper" role="img" aria-label="Crumpled black paper texture"></div>
    <div class="card__edge card__edge--left"></div>
    <div class="card__edge card__edge--right"></div>
    <div class="brand-name">Lantern Bay Media</div>
    <div class="divider"></div>
    <div class="contact">
      <p class="contact__name">Mark Dellweather</p>
      <p class="contact__title">Producer/CEO</p>
      <ul class="contact__lines">
        <li>C. 949-555-0147</li>
        <li>F. 650-555-0193</li>
        <li>markd@lanternbay.example</li>
      </ul>
    </div>
  </section>
  <p class="side-label side-label--back">back</p>
</body>
</html>
```